IT services provider needs a go to market lifecycle design

We need our go to market lifecycle diagram to be developed to show the flow of our propositions. We believe that customers could engage us at any stage of the cycle and that it would lead on to the next proposition, or, they could join at the start (Assess and Advice) and we would provide them with our services throughout the cycle.

```html
<!DOCTYPE html>
<html lang="en">
<head>
<meta charset="utf-8">
<title>Brightcore Cloudspace – Go to Market Lifecycle</title>
<link rel="stylesheet" href="https://fonts.googleapis.com/css2?family=Anton&family=Archivo+Black&display=swap">
<style>
  :root {
    --bg: #ffffff;
    --assess-dark: #55278c;
    --assess-light: #7c48b4;
    --architect-dark: #6536bb;
    --architect-light: #8b63d8;
    --manage-dark: #9572da;
    --manage-light: #b89be9;
    --recycle-dark: #b7a5ee;
    --recycle-light: #d9cff8;
    --label: #ffffff;
    --core-red: #e3262c;
    --core-red-deep: #9e1418;
  }
  * { margin: 0; padding: 0; box-sizing: border-box; }
  html, body { width: 1200px; height: 1200px; overflow: hidden; background: var(--bg); }
  .lifecycle { position: relative; width: 1200px; height: 1200px; }
  .lifecycle-ring { position: absolute; inset: 0; width: 1200px; height: 1200px; }
  .stage-shape { filter: drop-shadow(0 6px 8px rgba(40, 10, 80, 0.35)); }
  .stage-label {
    font-family: "Archivo Black", "Arial Black", sans-serif;
    fill: var(--label);
    text-transform: uppercase;
  }
  .stage-label--main { font-size: 58px; letter-spacing: 4px; }
  .stage-label--sub { font-size: 38px; letter-spacing: 1px; }
  .stage-label--even { font-size: 48px; letter-spacing: 3px; }
  .stage-label--lead { font-size: 56px; letter-spacing: 3px; }
  .ring-hole { fill: #f6f4fa; }
  .core-title {
    position: absolute;
    left: 0;
    width: 1200px;
    text-align: center;
    font-family: "Anton", "Impact", sans-serif;
    font-size: 94px;
    line-height: 1;
    color: var(--core-red);
    letter-spacing: 1px;
    text-shadow:
      1px 1px 0 var(--core-red-deep),
      2px 2px 0 var(--core-red-deep),
      3px 3px 0 var(--core-red-deep),
      4px 4px 0 var(--core-red-deep),
      5px 5px 0 var(--core-red-deep),
      6px 9px 10px rgba(0, 0, 0, 0.3);
  }
  .core-title--top { top: 500px; }
  .core-title--bottom { top: 602px; }
</style>
</head>
<body>
<main class="lifecycle">
  <svg class="lifecycle-ring" viewBox="0 0 1200 1200" xmlns="http://www.w3.org/2000/svg" aria-label="Lifecycle: Assess and Advise, Architect and Transform, Manage and Operate, Recycle and Retire">
    <defs>
      <path id="stage-arrow" d="M607.85,150.07 A450,450 0 0 1 1049.93,592.15 L962.28,644.48 L879.96,595.11 A280,280 0 0 0 604.89,320.04 L650.80,238.55 Z"/>
      <linearGradient id="grad-assess" x1="0" y1="0" x2="1" y2="1">
        <stop offset="0" stop-color="var(--assess-dark)"/><stop offset="1" stop-color="var(--assess-light)"/>
      </linearGradient>
      <linearGradient id="grad-architect" x1="0" y1="0" x2="1" y2="1">
        <stop offset="0" stop-color="var(--architect-dark)"/><stop offset="1" stop-color="var(--architect-light)"/>
      </linearGradient>
      <linearGradient id="grad-manage" x1="0" y1="0" x2="1" y2="1">
        <stop offset="0" stop-color="var(--manage-dark)"/><stop offset="1" stop-color="var(--manage-light)"/>
      </linearGradient>
      <linearGradient id="grad-recycle" x1="0" y1="0" x2="1" y2="1">
        <stop offset="0" stop-color="var(--recycle-dark)"/><stop offset="1" stop-color="var(--recycle-light)"/>
      </linearGradient>

      <path id="arc-assess-outer" d="M209.49,565.83 A392,392 0 0 1 565.83,209.49"/>
      <path id="arc-assess-inner" d="M263.29,570.54 A338,338 0 0 1 570.54,263.29"/>
      <path id="arc-architect-outer" d="M634.17,209.49 A392,392 0 0 1 990.51,565.83"/>
      <path id="arc-architect-inner" d="M629.46,263.29 A338,338 0 0 1 936.71,570.54"/>
      <path id="arc-manage-inner" d="M630.94,953.65 A355,355 0 0 0 953.65,630.94"/>
      <path id="arc-manage-outer" d="M635.74,1008.44 A410,410 0 0 0 1008.44,635.74"/>
      <path id="arc-recycle-inner" d="M246.35,630.94 A355,355 0 0 0 569.06,953.65"/>
      <path id="arc-recycle-outer" d="M191.56,635.74 A410,410 0 0 0 564.26,1008.44"/>
    </defs>

    <circle class="ring-hole" cx="600" cy="600" r="280"/>

    <g class="stage-shape">
      <use href="#stage-arrow" fill="url(#grad-recycle)" transform="rotate(180 600 600)"/>
      <use href="#stage-arrow" fill="url(#grad-manage)" transform="rotate(90 600 600)"/>
      <use href="#stage-arrow" fill="url(#grad-architect)"/>
      <use href="#stage-arrow" fill="url(#grad-assess)" transform="rotate(270 600 600)"/>
    </g>

    <g class="stage stage--assess">
      <text class="stage-label stage-label--main"><textPath href="#arc-assess-outer" startOffset="50%" text-anchor="middle">Assess</textPath></text>
      <text class="stage-label stage-label--sub"><textPath href="#arc-assess-inner" startOffset="50%" text-anchor="middle">&amp; Advise</textPath></text>
    </g>
    <g class="stage stage--architect">
      <text class="stage-label stage-label--main"><textPath href="#arc-architect-outer" startOffset="50%" text-anchor="middle">Architect</textPath></text>
      <text class="stage-label stage-label--sub"><textPath href="#arc-architect-inner" startOffset="50%" text-anchor="middle">&amp; Transform</textPath></text>
    </g>
    <g class="stage stage--manage">
      <text class="stage-label stage-label--even"><textPath href="#arc-manage-inner" startOffset="50%" text-anchor="middle">Manage</textPath></text>
      <text class="stage-label stage-label--lead"><textPath href="#arc-manage-outer" startOffset="50%" text-anchor="middle">&amp; Operate</textPath></text>
    </g>
    <g class="stage stage--recycle">
      <text class="stage-label stage-label--even"><textPath href="#arc-recycle-inner" startOffset="50%" text-anchor="middle">Recycle</textPath></text>
      <text class="stage-label stage-label--lead"><textPath href="#arc-recycle-outer" startOffset="50%" text-anchor="middle">&amp; Retire</textPath></text>
    </g>
  </svg>

  <h1 class="core-title core-title--top">BRIGHTCORE</h1>
  <p class="core-title core-title--bottom">CLOUDSPACE</p>
</main>
</body>
</html>
```